Banner Ad for website hompage - Design Project

We need 4 banner ads for the homepage of a Rent a Car company based in dubai. We rent a wide range of cars but mainly deal in the affordable cars category. Our website colors are mainly red, white and black and I can send pictures of the website (attached) if you want something to compare possible design ideas with. The banners need to promote different messages and must be appealing to the end user. It must also use pictures of cars that exist in our fleet (Pls note: this is only if you are using cars in the banner ad)

The 4 banner ads needed are as follows:
1) should promote something along the lines of we have 20+ models available and reserve a car now (This banner should also have a reserve now button, not the actual button but it's design. The button will be made and coded by us)
2) should promote something along the lines of we offer personalised service and we look after each and every custoemr individually
3) we provide attractive rates based on daily, weekly, monthly and longer rental periods (should also incorporate a reserve now message)
4) Like us on quorvia and follow us on social media for additional offers and discounts (would like for this to have a like button design implemented in it which will be linked to quorvia.)

Also please not the picture file size is 940pixels by 400pixels

Finally: I also need the psd files for the banners.

```html
<!DOCTYPE html>
<html lang="en">
<head>
<meta charset="utf-8">
<title>Rent a Car Homepage Banners</title>
<link rel="stylesheet" href="https://fonts.googleapis.com/css2?family=Noto+Sans:wght@300;400;700&family=Noto+Serif:wght@400&display=swap">
<style>
  :root {
    --backdrop: #262626;
    --brand-red: #d42a00;
    --brand-red-deep: #c01f00;
    --brand-red-dark: #8e1a00;
    --button-red: #c42400;
    --button-text: #8a1800;
    --frame-red: #e8553a;
    --white: #ffffff;
    --panel-grey: #f6f6f6;
    --photo-light: #eeeeee;
    --photo-mid: #c9c9c9;
    --ink: #1e1e1e;
    --like-blue: #3b5592;
  }
  * { box-sizing: border-box; margin: 0; padding: 0; }
  html, body { width: 900px; height: 1200px; overflow: hidden; }
  body { background: var(--backdrop); font-family: "Noto Sans", Arial, sans-serif; position: relative; }

  .banner { position: absolute; left: 143px; width: 636px; height: 269px; overflow: hidden; }
  .banner--models { top: 22px; background: var(--brand-red); }
  .banner--service { top: 316px; background: var(--white); }
  .banner--rates { top: 610px; height: 270px; background: var(--panel-grey); }
  .banner--social { top: 906px; background: var(--brand-red); }

  .abs { position: absolute; }

  /* Banner 1 */
  .models-headline { left: 12px; top: 62px; color: var(--white); line-height: 1; white-space: nowrap; }
  .models-headline .over { font-size: 36px; font-weight: 300; }
  .models-headline .count { font-size: 50px; font-weight: 700; }
  .models-rule { left: 12px; top: 120px; width: 203px; height: 3px; background: var(--white); }
  .models-sub { left: 12px; top: 126px; color: var(--white); font-size: 27px; white-space: nowrap; }
  .models-sub strong { font-weight: 700; }
  .reserve-button {
    background: var(--button-red); color: var(--button-text); font-weight: 700;
    letter-spacing: 9px; text-align: center; border-radius: 4px;
    box-shadow: 0 2px 0 rgba(0,0,0,0.25), inset 0 1px 0 rgba(255,255,255,0.15);
  }
  .models-reserve { left: 12px; top: 173px; width: 215px; height: 48px; line-height: 48px; font-size: 24px; }
  .models-cta { left: 42px; top: 229px; color: var(--white); font-size: 25px; white-space: nowrap; }
  .models-cta strong { font-weight: 700; }
  .car-photo {
    border: 5px solid var(--frame-red);
    background: linear-gradient(160deg, var(--white), var(--photo-light) 55%, var(--photo-mid));
  }
  .photo-1 { left: 233px; top: 33px; width: 187px; height: 97px; }
  .photo-2 { left: 435px; top: 8px; width: 192px; height: 101px; }
  .photo-3 { left: 270px; top: 146px; width: 155px; height: 117px; }
  .photo-4 { left: 437px; top: 122px; width: 160px; height: 113px; }

  /* Banner 2 */
  .service-strip {
    background: var(--brand-red); color: var(--white); font-weight: 700; font-size: 26px;
    white-space: nowrap; padding: 0 9px; height: 47px; line-height: 47px;
  }
  .service-strip em { font-style: normal; color: var(--button-text); }
  .strip-1 { left: 172px; top: 8px; width: 367px; transform: rotate(-1.2deg); }
  .strip-2 { left: 82px; top: 70px; width: 365px; transform: rotate(-1deg); }
  .strip-3 { left: 10px; top: 131px; width: 262px; transform: rotate(-1.2deg); }
  .strip-4 { left: 7px; top: 192px; width: 318px; transform: rotate(-1deg); }
  .service-photo { left: 318px; top: 126px; width: 318px; height: 143px;
    background: radial-gradient(ellipse at 55% 55%, var(--photo-mid), var(--photo-light) 60%, var(--white) 80%); }

  /* Banner 3 */
  .rates-shape { left: 0; top: 0; }
  .rates-title { left: 5px; top: 17px; color: var(--white); font-weight: 700; font-size: 26px; white-space: nowrap; }
  .rates-list { left: 16px; top: 82px; list-style: none; }
  .rates-list li { display: flex; align-items: center; height: 40px; color: var(--white); font-weight: 700; font-size: 26px; white-space: nowrap; }
  .rates-list svg { width: 42px; height: 40px; margin-right: 10px; flex: none; }
  .rates-cta { left: 484px; top: 110px; color: var(--button-text); font-weight: 700; font-size: 21px; white-space: nowrap; }
  .rates-reserve { left: 473px; top: 146px; width: 161px; height: 36px; line-height: 36px; font-size: 19px; letter-spacing: 7px; }

  /* Banner 4 */
  .social-shape { left: 0; top: 0; }
  .social-lead { left: 0; width: 636px; top: 50px; text-align: center; font-family: "Noto Serif", Georgia, serif; font-size: 27px; color: var(--ink); }
  .social-row { left: 168px; top: 112px; display: flex; gap: 8px; }
  .social-item { width: 53px; display: flex; flex-direction: column; align-items: center; gap: 4px; }
  .social-item .mark { width: 48px; height: 48px; border-radius: 6px; }
  .social-item .name { font-family: "Noto Serif", Georgia, serif; font-size: 11px; color: var(--ink); }
  .mark--chirply { background: #4fb7e3; }
  .mark--quorvia { background: #3b5592; }
  .mark--worknet { background: #2a87bd; }
  .mark--feedline { background: #f08a1e; }
  .mark--circlo { background: #2a2a2a; }
  .like-line { left: 0; width: 636px; top: 183px; display: flex; justify-content: center; align-items: center; gap: 12px;
    font-family: "Noto Serif", Georgia, serif; font-size: 29px; color: var(--like-blue); }
  .like-line .mark { width: 40px; height: 40px; background: var(--like-blue); border-radius: 4px; }
</style>
</head>
<body>

<section class="banner banner--models">
  <div class="abs models-headline"><span class="over">over </span><span class="count">20+</span></div>
  <div class="abs models-rule"></div>
  <div class="abs models-sub">vehicle <strong>MODELS</strong></div>
  <div class="abs reserve-button models-reserve">RESERVE</div>
  <div class="abs models-cta">a car <strong>NOW</strong></div>
  <div class="abs car-photo photo-1" role="img" aria-label="Photo of a black sedan from the fleet"></div>
  <div class="abs car-photo photo-2" role="img" aria-label="Photo of a silver compact sedan from the fleet"></div>
  <div class="abs car-photo photo-3" role="img" aria-label="Photo of a white sedan from the fleet"></div>
  <div class="abs car-photo photo-4" role="img" aria-label="Photo of a red sedan from the fleet"></div>
</section>

<section class="banner banner--service">
  <div class="abs service-strip strip-1">we offer <em>PERSONALIZED</em></div>
  <div class="abs service-strip strip-2">service and we look after</div>
  <div class="abs service-strip strip-3"><em>EACH</em> and <em>EVERY</em></div>
  <div class="abs service-strip strip-4">customer individually</div>
  <div class="abs service-photo" role="img" aria-label="Photo of a silver compact sedan"></div>
</section>

<section class="banner banner--rates">
  <svg class="abs rates-shape" width="636" height="270" viewBox="0 0 636 270">
    <defs>
      <linearGradient id="ratesRed" x1="0" y1="0" x2="0" y2="1">
        <stop offset="0" stop-color="#df3400"/>
        <stop offset="1" stop-color="#c11e00"/>
      </linearGradient>
    </defs>
    <path d="M0 0 H467 C462 90 450 190 425 270 H0 Z" fill="url(#ratesRed)"/>
    <path d="M467 0 C462 90 450 190 425 270 H432 C457 190 469 90 474 0 Z" fill="var(--brand-red-dark)" opacity="0.6"/>
  </svg>
  <div class="abs rates-title">ATTRACTIVE RATES BASED ON:</div>
  <ul class="abs rates-list">
    <li><svg viewBox="0 0 42 40"><path d="M2 20 L12 16 L18 26 L36 2 L40 6 L18 38 Z" fill="var(--brand-red-dark)"/></svg>daily</li>
    <li><svg viewBox="0 0 42 40"><path d="M2 20 L12 16 L18 26 L36 2 L40 6 L18 38 Z" fill="var(--brand-red-dark)"/></svg>weekly</li>
    <li><svg viewBox="0 0 42 40"><path d="M2 20 L12 16 L18 26 L36 2 L40 6 L18 38 Z" fill="var(--brand-red-dark)"/></svg>monthly</li>
    <li><svg viewBox="0 0 42 40"><path d="M2 20 L12 16 L18 26 L36 2 L40 6 L18 38 Z" fill="var(--brand-red-dark)"/></svg>and longer rental periods</li>
  </ul>
  <div class="abs rates-cta">get your car</div>
  <div class="abs reserve-button rates-reserve">RESERVE</div>
</section>

<section class="banner banner--social">
  <svg class="abs social-shape" width="636" height="269" viewBox="0 0 636 269">
    <path d="M108 0 H528 C575 60 575 200 552 269 H78 C50 200 60 60 108 0 Z" fill="var(--brand-red-deep)"/>
    <path d="M118 0 H518 C560 60 560 200 540 269 H90 C66 200 76 60 118 0 Z" fill="var(--white)"/>
  </svg>
  <div class="abs social-lead">for additional offers:</div>
  <div class="abs social-row">
    <div class="social-item"><span class="mark mark--chirply"></span><span class="name">Chirply</span></div>
    <div class="social-item"><span class="mark mark--quorvia"></span><span class="name">quorvia</span></div>
    <div class="social-item"><span class="mark mark--worknet"></span><span class="name">Worknet</span></div>
    <div class="social-item"><span class="mark mark--feedline"></span><span class="name">Feedline</span></div>
    <div class="social-item"><span class="mark mark--circlo"></span><span class="name">Circlo</span></div>
  </div>
  <div class="abs like-line"><span class="mark"></span><span>Like us on quorvia</span></div>
</section>

</body>
</html>
```